TOPページのイメージを作成していただきたいです。
女性が入りやすく、親しみやすい色使いとフォントで、
カテゴリのボタンはアイコン等を使い、やわらかい印象を与えたい
※アイコンを指定しているわけではありません。

商品にカラフルなものが多くなりやすいので、全体的な色バランスはシンプルなカラーでお願いします。
サイドバナーとメインに上記スクールをターゲットとしたカテゴリに飛ぶためのバナー用意してほしいです。
近いサイトイメージは合わせて送らせていただきます。
スマートフォンでも表示させやすいレイアウトを希望します。
Quelvoのショッピングに関しては、Quelvoプリズマを契約予定です。
また、今回はトップページだけですが、契約させて頂いた方には商品ページなどサブページも依頼する可能性が高いです

-------------------
項目について
-------------------
※スプレッドシート参照
https://sheets.tavrolink.com/spreadsheets/d/7pxQwLzNc4bTr2VhYk9MeJsA8uDfGiHo3nKyRtE5WqPl/edit?usp=sharing
■ヘッダー
検索窓、お支払いについて、送料、お届けについて、返品、交換、保証について、会社概要、プライバシーポリシー、お問い合わせ、よくある質問
■フッター
店舗内簡易情報として、イメージ画像のような下記の内容を用意する予定で、記述箇所のデザインを用意してください
送料について、支払い方法について、手数料、納期、キャンセルについて、商品の在庫について
■カテゴリ
カテゴリは、別紙の資料の通りです。
大カテゴリがメイン、中に小カテゴリがあります。

■写真資料
https://files.tavrolink.com/file/d/9kd3RwQ7mZ2xVbN8pLcT4yHsJfGeAu6Wn/view?usp=sharing

■サイト見本イメージ
https://store.mirubeta.jp/pastelnook/
https://yarn-lumio.com/
https://ec.stitchvale.jp/
https://www.tomiseki.co.jp/shop/c/c10/
https://www.webshop.mirel-kasano.com/
https://works.brevok.net/
サイトの色合いや雰囲気に近いサイトになります。
1ページ
赤系、黄・オレンジ系、茶系
• イラストレーター形式 (.ai)
幅1250px程度
※Quelvoショップのバナーサイズを考慮しています。
場合によってはその他のページもお願いする可能性があります。
もう少し提案数を頂きたいため、5月13日(金)までコンペの延長をいたします。

今回選ばせていただきました理由は
・商品を邪魔しないシンプルさ
・Quelvoショップに落とし込んだ時に差異が生まれにくい点
・全体的な色使い
を中心に選ばせていただきました。
非常にあたたかく、親しみやすいデザインで作成いただきましたので、こちらに決定させていただきました。

今回いただきました提案はどれも素晴らしく、選考は非常に悩みました。
冒険するか、無難なデザインにするか、また、その中でもどれがいいか、かなり悩みまして、選ばれなかったデザインも、最後までの残ったデザインがいくつかございました。
本当に皆様ご提案ありがとうございました。
また次の機会がございましたら、是非よろしくお願いします。

```html
<!DOCTYPE html>
<html lang="ja">
<head>
<meta charset="utf-8">
<title>ハンドメイドshop こもれび</title>
<link rel="stylesheet" href="https://fonts.googleapis.com/css2?family=M+PLUS+Rounded+1c:wght@400;500;700&family=Noto+Sans+JP:wght@300;400;700&display=swap">
<style>
:root{
  --salmon:#f9c1ad;
  --pink-line:#f4b3a6;
  --purple-line:#b99ac4;
  --text:#444;
  --price:#e0302f;
  --teal:#6fc6c5;
  --peach:#f8b9a4;
  --rose:#e8a4ad;
  --lilac:#b293bd;
  --gray-panel:#9e9e9e;
}
*{box-sizing:border-box;margin:0;padding:0}
html,body{width:1200px;height:3881px;overflow:hidden;background:#fff}
body{position:relative;font-family:"Noto Sans JP",sans-serif;color:var(--text)}
.nowrap{white-space:nowrap}

/* header */
.site-header{position:absolute;left:0;top:0;width:1200px;height:68px}
.logo{position:absolute;left:18px;top:26px;font-family:"M PLUS Rounded 1c",sans-serif;font-weight:500;font-size:18px;color:#555;white-space:nowrap}
.search{position:absolute;left:290px;top:24px;width:615px;height:38px;border:2px solid #999;display:flex}
.search-field{flex:1;background:#fff}
.search-btn{width:60px;background:#888;display:flex;align-items:center;justify-content:center}
.cat-menu{position:absolute;left:940px;top:18px;width:60px;text-align:center;font-size:11px;color:#555;white-space:nowrap}
.cat-menu svg{display:block;margin:0 auto 3px}
.global-nav{position:absolute;left:0;top:68px;width:1200px;height:38px;background:var(--salmon);display:flex;align-items:center}
.global-nav a{flex:1;text-align:center;font-size:13px;color:#555;text-decoration:none;border-right:1px solid #8a6a60;line-height:20px;white-space:nowrap}
.global-nav a:last-child{border-right:none}

/* hero */
.hero{position:absolute;left:0;top:135px;width:1200px;height:410px}
.slide-side-left{position:absolute;left:0;top:0;width:192px;height:410px;background:var(--gray-panel);display:flex;align-items:center;justify-content:center;font-size:30px;color:#222}
.slide-main{position:absolute;left:292px;top:0;width:615px;height:410px;background:linear-gradient(135deg,#9a9590 0%,#c9c3ba 45%,#e7e2db 100%);overflow:hidden}
.slide-main .photo{position:absolute;inset:0}
.slide-main .catch{position:absolute;left:22px;top:55px;transform:rotate(-18deg);font-family:"M PLUS Rounded 1c",sans-serif;font-size:34px;color:#444;font-weight:700;white-space:nowrap}
.slide-main .catch small{font-size:20px;font-weight:500}
.slide-main .title{position:absolute;left:245px;top:38px;font-family:"M PLUS Rounded 1c",sans-serif;font-weight:700;font-size:48px;color:#fff;white-space:nowrap;line-height:1.1}
.slide-main .lead{position:absolute;left:282px;top:110px;font-size:16px;color:#fff;font-weight:700;white-space:nowrap}
.slide-main .heart{position:absolute;left:285px;top:170px;width:280px;height:210px;border-radius:110px 110px 140px 140px;background:rgba(255,255,255,.55);display:flex;flex-direction:column;align-items:center;justify-content:center;font-family:"M PLUS Rounded 1c",sans-serif;color:#555;font-weight:700;white-space:nowrap}
.heart .big{font-size:44px}
.heart .mid{font-size:26px}
.slide-side-right{position:absolute;left:1007px;top:0;width:193px;height:410px;background:var(--salmon);overflow:hidden;font-family:"M PLUS Rounded 1c",sans-serif;white-space:nowrap}
.slide-side-right .t1{position:absolute;left:30px;top:50px;transform:rotate(-15deg);font-size:24px;color:#fff;font-weight:700;line-height:1.2}
.slide-side-right .t2{position:absolute;left:8px;top:150px;transform:rotate(-15deg);font-size:68px;color:#4f8f8a;font-weight:700;line-height:1.05}
.slide-side-right .t3{position:absolute;left:10px;top:355px;font-size:22px;color:#444;font-weight:700}
.arrow{position:absolute;top:178px;width:52px;height:52px;border-radius:50%;background:#d9d9d9;display:flex;align-items:center;justify-content:center}
.arrow.prev{left:216px}
.arrow.next{left:930px}
.dots{position:absolute;left:540px;top:566px;display:flex;gap:38px}
.dots span{width:13px;height:13px;border-radius:50%;background:#bbb}
.dots span:first-child{background:#555}
.divider{position:absolute;left:24px;top:603px;width:1152px;border-top:3px dashed var(--pink-line)}

/* sidebar */
.sidebar{position:absolute;left:18px;top:643px;width:270px}
.side-banner{display:block;width:270px;height:180px;margin-bottom:20px;position:relative;overflow:hidden;font-family:"M PLUS Rounded 1c",sans-serif;white-space:nowrap}
.side-banner.event{background:linear-gradient(135deg,#9a9590,#d8d2ca)}
.side-banner.event .b1{position:absolute;left:108px;top:14px;font-size:22px;color:#fff;font-weight:700}
.side-banner.event .b2{position:absolute;left:110px;top:46px;font-size:8px;color:#fff}
.side-banner.event .b3{position:absolute;left:120px;top:70px;width:130px;height:95px;border-radius:50px;background:rgba(255,255,255,.55);display:flex;align-items:center;justify-content:center;text-align:center;font-size:16px;color:#555;font-weight:700;line-height:1.2}
.side-banner.start{background:linear-gradient(135deg,#f8c3b0,#d9a996)}
.side-banner.start .b1{position:absolute;left:4px;top:55px;transform:rotate(-14deg);font-size:36px;color:#4f8f8a;font-weight:700;line-height:1.1}
.side-banner.start .b2{position:absolute;left:6px;top:155px;font-size:9px;color:#444;font-weight:700}
.cat-heading{margin-top:28px;height:45px;background:var(--salmon);color:#fff;font-family:"M PLUS Rounded 1c",sans-serif;font-weight:700;font-size:24px;padding-left:20px;line-height:45px;white-space:nowrap}
.cat-list{list-style:none;margin-top:14px}
.cat-group{margin-bottom:10px}
.cat-major{display:flex;align-items:center;height:32px;font-size:19px;color:#444;white-space:nowrap}
.cat-icon{width:46px;height:36px;margin-right:20px;display:block;flex:none}
.cat-sub{list-style:none}
.cat-sub li{height:29px;line-height:29px;padding-left:105px;font-size:16px;color:#555;white-space:nowrap}

/* main */
.main{position:absolute;left:327px;top:0;width:836px}
.section-title{position:absolute;left:0;width:836px;font-size:21px;color:#555;font-weight:400;padding-bottom:6px;border-bottom:3px dashed var(--purple-line)}
.products{position:absolute;left:0;display:flex;gap:21px}
.product{width:194px}
.product .thumb{width:194px;height:193px;display:block}
.product .name{margin-top:18px;font-size:12px;line-height:16px;color:#555;white-space:nowrap}
.product .price{margin-top:10px;font-size:20px;font-weight:700;color:var(--price)}
.product .price small{font-size:12px;font-weight:400;color:#555;margin-left:4px}
.guide{position:absolute;left:0;top:2209px;width:836px;display:grid;grid-template-columns:405px 405px;gap:23px 21px}
.guide a{height:99px;border-radius:12px;display:flex;align-items:center;justify-content:center;color:#fff;text-decoration:none;font-family:"M PLUS Rounded 1c",sans-serif;font-weight:700;font-size:30px;white-space:nowrap;box-shadow:0 3px 5px rgba(0,0,0,.15)}
.guide a.long{font-size:26px}
.guide a small{font-size:14px;margin-left:4px}
.g-teal{background:var(--teal)}
.g-peach{background:var(--peach)}
.g-rose{background:var(--rose)}
.g-lilac{background:var(--lilac)}

/* footer */
.site-footer{position:absolute;left:0;top:2964px;width:1200px;height:917px;background:var(--salmon)}
.info-panel{position:absolute;top:33px;width:480px;height:791px;background:#fff;padding:20px 20px}
.info-panel.left{left:105px}
.info-panel.right{left:614px}
.info-block{margin-bottom:26px}
.info-block h3{font-size:16px;font-weight:400;color:#555;padding-bottom:3px;border-bottom:3px dotted var(--pink-line);width:340px;margin-bottom:6px}
.info-block p{font-size:11.5px;line-height:1.5;color:#444}
.info-block p+p{margin-top:12px}
.cards{display:flex;gap:8px;margin:4px 0 4px 14px}
.cards span{width:32px;height:22px;background:#d8d8d8;border-radius:2px}
</style>
</head>
<body>

<header class="site-header">
  <div class="logo">ハンドメイドshop こもれび</div>
  <div class="search"><div class="search-field"></div><div class="search-btn">
    <svg width="26" height="26" viewBox="0 0 26 26"><circle cx="11" cy="11" r="8" fill="none" stroke="#fff" stroke-width="3"/><line x1="17" y1="17" x2="24" y2="24" stroke="#fff" stroke-width="3"/></svg>
  </div></div>
  <div class="cat-menu">
    <svg width="26" height="26" viewBox="0 0 26 26" fill="#555"><rect x="0" y="0" width="7" height="7"/><rect x="9.5" y="0" width="7" height="7"/><rect x="19" y="0" width="7" height="7"/><rect x="0" y="9.5" width="7" height="7"/><rect x="9.5" y="9.5" width="7" height="7"/><rect x="19" y="9.5" width="7" height="7"/><rect x="0" y="19" width="7" height="7"/><rect x="9.5" y="19" width="7" height="7"/><rect x="19" y="19" width="7" height="7"/></svg>
    カテゴリー
  </div>
</header>
<nav class="global-nav">
  <a href="#">お支払いについて</a><a href="#">送料・お届けについて</a><a href="#">返品・交換・保証について</a><a href="#">会社概要</a><a href="#">プライバシーポリシー</a><a href="#">よくある質問</a><a href="#">お問い合わせ</a>
</nav>

<section class="hero">
  <div class="slide-side-left">未</div>
  <div class="slide-main">
    <div class="photo" role="img" aria-label="机に向かって色ペンで絵を描く子どもの写真"></div>
    <div class="catch"><small>初めてでも</small>簡単</div>
    <div class="title">イベントキッド</div>
    <div class="lead">子供向けイベント・モノづくり体験に</div>
    <div class="heart"><span class="big">自分だけ</span><span class="mid">のアイテムが</span><span class="mid">作れる！</span></div>
  </div>
  <div class="slide-side-right">
    <div class="t1">子供向けイベ<br>モノづくり</div>
    <div class="t2">スター<br>キッ</div>
    <div class="t3">初めてでも「簡単</div>
  </div>
  <div class="arrow prev"><svg width="34" height="16" viewBox="0 0 34 16"><path d="M33 8H3M10 1L2 8l8 7" fill="none" stroke="#fff" stroke-width="2.5"/></svg></div>
  <div class="arrow next"><svg width="34" height="16" viewBox="0 0 34 16"><path d="M1 8h30M24 1l8 7-8 7" fill="none" stroke="#fff" stroke-width="2.5"/></svg></div>
</section>
<div class="dots"><span></span><span></span><span></span></div>
<div class="divider"></div>

<aside class="sidebar">
  <a class="side-banner event" role="img" aria-label="イベントキッドのバナー：絵を描く子どもの写真">
    <span class="b1">イベントキッド</span><span class="b2">子供向けイベント・モノづくり体験に</span>
    <span class="b3">自分だけ<br>のアイテムが<br>作れる！</span>
  </a>
  <a class="side-banner start" role="img" aria-label="スタートキットのバナー：工作をする子どもたちの写真">
    <span class="b1">スタート<br>キット</span><span class="b2">初めてでも「簡単」に「自分だけ」のアイテムが作れる</span>
  </a>
  <div class="cat-heading">カテゴリーから探す</div>
  <ul class="cat-list">
    <li class="cat-group"><div class="cat-major"><svg class="cat-icon" role="img" aria-label="装飾用品のアイコン"><rect x="4" y="2" width="38" height="32" rx="8" fill="#e6e6e6"/></svg>装飾用品</div>
      <ul class="cat-sub"><li>アイロン接着</li><li>お得な業務用シート</li><li>ホットメルト用品</li></ul></li>
    <li class="cat-group"><div class="cat-major"><svg class="cat-icon" role="img" aria-label="染色・ペイント・プリントのアイコン"><rect x="4" y="2" width="38" height="32" rx="8" fill="#e6e6e6"/></svg>染色・ペイント・プリント</div>
      <ul class="cat-sub"><li>プリント用紙</li><li>インク</li><li>ペン・筆記用具</li><li>ライトボックス</li><li>プリンター</li></ul></li>
    <li class="cat-group"><div class="cat-major"><svg class="cat-icon" role="img" aria-label="加工機器のアイコン"><rect x="4" y="2" width="38" height="32" rx="8" fill="#e6e6e6"/></svg>加工機器</div>
      <ul class="cat-sub"><li>プレス機</li></ul></li>
    <li class="cat-group"><div class="cat-major"><svg class="cat-icon" role="img" aria-label="無地素材のアイコン"><rect x="4" y="2" width="38" height="32" rx="8" fill="#e6e6e6"/></svg>無地素材</div>
      <ul class="cat-sub"><li>T シャツ</li><li>バッグ</li><li>昇華ペン対応</li><li>業務用生地</li></ul></li>
    <li class="cat-group"><div class="cat-major"><svg class="cat-icon" role="img" aria-label="加工道具のアイコン"><rect x="4" y="2" width="38" height="32" rx="8" fill="#e6e6e6"/></svg>加工道具</div>
      <ul class="cat-sub"><li>シート加工用品</li><li>プレス加工用品</li><li>テープ</li></ul></li>
    <li class="cat-group"><div class="cat-major"><svg class="cat-icon" role="img" aria-label="カット道具のアイコン"><rect x="4" y="2" width="38" height="32" rx="8" fill="#e6e6e6"/></svg>カット道具</div>
      <ul class="cat-sub"><li>デザインナイフ</li><li>クラフトパンチ</li><li>ダイカットマシン</li><li>カッターマット</li><li>プロッター</li><li>プロッター消耗品</li></ul></li>
    <li class="cat-group"><div class="cat-major"><svg class="cat-icon" role="img" aria-label="捨て紙のアイコン"><rect x="4" y="2" width="38" height="32" rx="8" fill="#e6e6e6"/></svg>捨て紙</div>
      <ul class="cat-sub"><li>アイロンプリント用</li><li>昇華転写用</li></ul></li>
    <li class="cat-group"><div class="cat-major"><svg class="cat-icon" role="img" aria-label="縫製のアイコン"><rect x="4" y="2" width="38" height="32" rx="8" fill="#e6e6e6"/></svg>縫製</div>
      <ul class="cat-sub"><li>ミシン</li><li>スタートキット</li><li>イベントキット</li><li>その他</li></ul></li>
    <li class="cat-group"><div class="cat-major"><svg class="cat-icon" role="img" aria-label="Tシャツ作成のアイコン"><rect x="4" y="2" width="38" height="32" rx="8" fill="#e6e6e6"/></svg>T シャツ作成</div>
      <ul class="cat-sub"><li>スタートキット</li><li>イベントキット</li></ul></li>
    <li class="cat-group"><div class="cat-major"><svg class="cat-icon" role="img" aria-label="バッグ作成のアイコン"><rect x="4" y="2" width="38" height="32" rx="8" fill="#e6e6e6"/></svg>バッグ作成</div>
      <ul class="cat-sub"><li>スタートキット</li><li>イベントキット</li></ul></li>
    <li class="cat-group"><div class="cat-major"><svg class="cat-icon" role="img" aria-label="アイロンシート作成のアイコン"><rect x="4" y="2" width="38" height="32" rx="8" fill="#e6e6e6"/></svg>アイロンシートを作成</div>
      <ul class="cat-sub"><li>アイロン転写シート</li><li>プロッター</li><li>プリント用紙</li></ul></li>
    <li class="cat-group"><div class="cat-major"><svg class="cat-icon" role="img" aria-label="イベントキットのアイコン"><rect x="4" y="2" width="38" height="32" rx="8" fill="#e6e6e6"/></svg>イベントキット</div>
      <ul class="cat-sub"><li>T シャツ作成</li><li>マグカップ作成</li><li>バッグ作成</li></ul></li>
    <li class="cat-group"><div class="cat-major"><svg class="cat-icon" role="img" aria-label="スタートキットのアイコン"><rect x="4" y="2" width="38" height="32" rx="8" fill="#e6e6e6"/></svg>スタートキット</div>
      <ul class="cat-sub"><li>T シャツ作成</li><li>マグカップ作成</li><li>バッグ作成</li><li>工作キット</li></ul></li>
  </ul>
</aside>

<main class="main">
  <h2 class="section-title" style="top:640px">おすすめアイテム</h2>
  <div class="products" style="top:693px">
    <div class="product"><div class="thumb" role="img" aria-label="ラメ入りの星形パーツの写真" style="background:linear-gradient(135deg,#8c8a8f,#b45bb0 55%,#d9d3dd)"></div><p class="name">商品名あいうえお商品名あいうえお<br>商品名あいうえお</p><p class="price">1,000 円<small>（税込）</small></p></div>
    <div class="product"><div class="thumb" role="img" aria-label="デニムに付けた蝶のラインストーンの写真" style="background:linear-gradient(135deg,#1e2b5a,#2f3f78 60%,#b69a48)"></div><p class="name">商品名あいうえお商品名あいうえお<br>商品名あいうえお</p><p class="price">1,000 円<small>（税込）</small></p></div>
    <div class="product"><div class="thumb" role="img" aria-label="カラフルなプリントの黒い服の写真" style="background:linear-gradient(135deg,#7a6a8a,#2a2a2e 55%,#b04a6a)"></div><p class="name">商品名あいうえお商品名あいうえお<br>商品名あいうえお</p><p class="price">1,000 円<small>（税込）</small></p></div>
    <div class="product"><div class="thumb" role="img" aria-label="海辺に置かれた帽子の写真" style="background:linear-gradient(180deg,#7ab8d8,#2a4a5a 55%,#3aa8b8)"></div><p class="name">商品名あいうえお商品名あいうえお<br>商品名あいうえお</p><p class="price">1,000 円<small>（税込）</small></p></div>
  </div>

  <h2 class="section-title" style="top:1015px">人気ランキング</h2>
  <div class="products" style="top:1068px">
    <div class="product"><div class="thumb" role="img" aria-label="水中の青いスイムキャップの写真" style="background:linear-gradient(135deg,#3a9fc8,#7dd0e6 60%,#2a5fa0)"></div><p class="name">商品名あいうえお商品名あいうえお<br>商品名あいうえお</p><p class="price">1,000 円<small>（税込）</small></p></div>
    <div class="product"><div class="thumb" role="img" aria-label="文字プリントの緑のTシャツの写真" style="background:linear-gradient(135deg,#4aa890,#1f6a5a 60%,#9ad0c0)"></div><p class="name">商品名あいうえお商品名あいうえお<br>商品名あいうえお</p><p class="price">1,000 円<small>（税込）</small></p></div>
    <div class="product"><div class="thumb" role="img" aria-label="青いリュックと文房具の写真" style="background:linear-gradient(135deg,#d8d8d8,#3a6fc0 55%,#e8e0d0)"></div><p class="name">商品名あいうえお商品名あいうえお<br>商品名あいうえお</p><p class="price">1,000 円<small>（税込）</small></p></div>
    <div class="product"><div class="thumb" role="img" aria-label="プリント入りのグレーTシャツの写真" style="background:linear-gradient(135deg,#c8c8c8,#8a8a8a 55%,#d8d8d8)"></div><p class="name">商品名あいうえお商品名あいうえお<br>商品名あいうえお</p><p class="price">1,000 円<small>（税込）</small></p></div>
  </div>

  <h2 class="section-title" style="top:1390px">新着アイテム</h2>
  <div class="products" style="top:1443px">
    <div class="product"><div class="thumb" role="img" aria-label="文字プリントの白いトートバッグの写真" style="background:linear-gradient(135deg,#9a9ea4,#e8e8e8 55%,#b8bcc0)"></div><p class="name">商品名あいうえお商品名あいうえお<br>商品名あいうえお</p><p class="price">1,000 円<small>（税込）</small></p></div>
    <div class="product"><div class="thumb" role="img" aria-label="白い文字入りの黒い布の写真" style="background:linear-gradient(135deg,#3a3a3a,#4a4a4a 55%,#2a2a2a)"></div><p class="name">商品名あいうえお商品名あいうえお<br>商品名あいうえお</p><p class="price">1,000 円<small>（税込）</small></p></div>
    <div class="product"><div class="thumb" role="img" aria-label="柄プリントのグレーTシャツの写真" style="background:linear-gradient(135deg,#a8a8a8,#d8d8d8 55%,#8a8a8a)"></div><p class="name">商品名あいうえお商品名あいうえお<br>商品名あいうえお</p><p class="price">1,000 円<small>（税込）</small></p></div>
    <div class="product"><div class="thumb" role="img" aria-label="ハンガーに掛けた白いTシャツの写真" style="background:linear-gradient(135deg,#b8b4ac,#f0f0f0 55%,#9a968e)"></div><p class="name">商品名あいうえお商品名あいうえお<br>商品名あいうえお</p><p class="price">1,000 円<small>（税込）</small></p></div>
  </div>

  <h2 class="section-title" style="top:1765px">セール品</h2>
  <div class="products" style="top:1818px">
    <div class="product"><div class="thumb" role="img" aria-label="落ち葉の上のトートバッグの写真" style="background:linear-gradient(135deg,#e8a030,#b85a10 55%,#f0c060)"></div><p class="name">商品名あいうえお商品名あいうえお<br>商品名あいうえお</p><p class="price">1,000 円<small>（税込）</small></p></div>
    <div class="product"><div class="thumb" role="img" aria-label="ギター柄の黒いTシャツの写真" style="background:linear-gradient(135deg,#6a6a6a,#1e1e24 55%,#8a8a8a)"></div><p class="name">商品名あいうえお商品名あいうえお<br>商品名あいうえお</p><p class="price">1,000 円<small>（税込）</small></p></div>
    <div class="product"><div class="thumb" role="img" aria-label="クリスマス柄のクッションの写真" style="background:linear-gradient(135deg,#a82020,#3a2a24 55%,#c89040)"></div><p class="name">商品名あいうえお商品名あいうえお<br>商品名あいうえお</p><p class="price">1,000 円<small>（税込）</small></p></div>
    <div class="product"><div class="thumb" role="img" aria-label="レンガ壁に掛けたパーカーの写真" style="background:linear-gradient(135deg,#c8c4bc,#9a5a48 55%,#5a6068)"></div><p class="name">商品名あいうえお商品名あいうえお<br>商品名あいうえお</p><p class="price">1,000 円<small>（税込）</small></p></div>
  </div>

  <h2 class="section-title" style="top:2156px">初めての方向けコンテンツ</h2>
  <div class="guide">
    <a href="#" class="g-teal long">シートのカットの方法について</a>
    <a href="#" class="g-peach long">シートの加工の仕方<small>（アイロン編）</small></a>
    <a href="#" class="g-rose">長く持たせるには</a>
    <a href="#" class="g-lilac">加工品の注意点</a>
  </div>
</main>

<footer class="site-footer">
  <div class="info-panel left">
    <div class="info-block">
      <h3>送料について</h3>
      <p>■宅配便<br>北海道 800 円・沖縄、離島 1,880 円・その他の地域 580 円<br>※合計 3,780 円（税込）以上のご購入で送料無料<br>※北海道・沖縄・離島は 580 円割引いたします。<br>※離島・一部地域は追加送料の場合がございます。</p>
      <p>■大型宅配便（巻き芯発送）<br>北海道 1,300 円・東北 1,200 円四国九州 1,150 円・沖縄、離島 2,000 円・<br>その他の地域 680 円<br>※合計 3,780 円（税込）以上のご購入で全地域 580 円割引、<br>合計 16,200 円（税込）以上のご購入で送料無料（沖縄のみ 500 円）<br>※離島・一部地域は追加送料の場合がございます。<br>・商品名に【巻き芯発送】と記載の商品を含むお買い物に限ります。</p>
      <p>■メール便<br>全国一律 250 円<br>※合計 3,780 円（税込）以上のご購入で送料無料<br>※離島・一部地域でも追加送料がかかりません。<br>・配送に掛かる日数…1 〜 2 日程度（遠方地は除く）<br>・お届け先に到着するまでの追跡サービス付き。<br>・商品ページに【メール便対応】と記載された商品に限ります。</p>
    </div>
    <div class="info-block">
      <h3>支払方法について</h3>
      <p>お支払い方法は下記の方法がございます。<br>■銀行振込<br>■クレジットカード</p>
      <div class="cards"><span></span><span></span><span></span></div>
      <div class="cards"><span></span><span></span><span></span></div>
      <p style="margin-top:0">■Quelvo! マネー / 預金払い<br>■代金引換<br>※代引手数料はお客様負担となります。</p>
    </div>
    <div class="info-block">
      <h3>手数料について</h3>
      <p>XXXXXXXXXXXXXXXXXXXXXXXXXXXXXXXXXXXXXXXXXXX<br>XXXXXXXXXXXXXXXXXXXXXXXXXXXXXXXXXXXXXXXXXXX<br>XXXXXXXXXXXXXXXXXXXXXXXXXXXXXXXXXXXXXXXXXXX</p>
    </div>
  </div>
  <div class="info-panel right">
    <div class="info-block" style="margin-bottom:70px">
      <h3>納期について</h3>
      <p>宅配でお届けする商品は、最短で翌日お届け（到着）いたします。<br>※複数口の場合は出荷が遅れる場合があります。<br>※在庫有り商品とお取り寄せ商品、または予約商品を、一緒にカートに入れてご注文された場合、全商品が揃い次第のお届けになります。お届け時に不在だった場合は、「ご不在連絡票」が投函されますので、記載されている青葉急便の連絡先へ、再配達のご依頼をお願いいたします。また出荷完了後、ご連絡のメールを送信いたします。<br>※出荷後の状況については、上記メール内の「青葉急便お荷物お問い合わせサービス」のリンクにてご確認ください。</p>
    </div>
    <div class="info-block" style="margin-bottom:40px">
      <h3>キャンセルについて</h3>
      <p>商品の発送には万全を期しておりますが、万が一、発送間違い、不良品などがございましたら正しい商品と交換させていただきます。</p>
      <p>■返品を受け付ける条件<br>未開封・未使用のもので、商品ご到着後 3 日以内に電話連絡いただいたもののみお受けいたします。</p>
      <p>■返品の送料・手数料の負担について<br>初期不良の場合は当社が負担いたします。お客様都合の場合はお客様にご負担いただきます。</p>
      <p>■生地のカット販売の返品について<br>お客様のオーダーに応じて、生地の裁断を行うという販売形式のため、生地のカット販売に関しましては、不良品を除く、お客様都合によるご注文後のキャンセル、返品交換はお断りしております。</p>
    </div>
    <div class="info-block">
      <h3>商品の在庫について</h3>
      <p>当サイトに掲載している商品は、複数店舗で同時に販売しております。その為、サイトよりご注文を頂いた時点で稀に他店舗にて完売してしまい欠品してしまう場合がございます。今後の入荷予定を確認して入荷が困難な場合は、誠に勝手ながらご注文をお取り消しさせて頂きます。<br>ご注文前の在庫確認につきましてはお電話またはメールにてお問合せいただくことをお勧めいたします。<br>在庫管理は、できる限りリアルタイムな更新を心がけておりますが、万一欠品の際はご了承下さい。</p>
    </div>
  </div>
</footer>

</body>
</html>
```